Website for Meadowlark Harvest Co

Slogan to be used is Fresh is Best !
I would like the website to be like my other business @ www.tuberworks.com.au. It is the same business

Vegetable Processing

Coded - Design and coding required

1 page

```html
<!DOCTYPE html>
<html lang="en">
<head>
<meta charset="utf-8">
<title>Meadowlark Harvest Co – Fresh is Best</title>
<link href="https://fonts.googleapis.com/css2?family=Lato:wght@400;700&family=Playfair+Display:ital,wght@0,700;0,900;1,400&display=swap" rel="stylesheet">
<style>
:root{
  --lime:#7fae1f;
  --lime-bright:#8cbf22;
  --header:#5f7f48;
  --heading:#5c7b44;
  --ink:#2b2b2b;
  --sidebar:#f4f8ee;
  --sidebar-head:#e8ece3;
  --page:#ececec;
  --white:#ffffff;
}
*{margin:0;padding:0;box-sizing:border-box}
html,body{width:1200px;height:1148px;overflow:hidden}
body{position:relative;background:var(--page);font-family:'Lato',sans-serif;color:var(--ink)}

.promo-bar{position:absolute;left:0;top:0;width:1200px;height:38px;background:var(--lime);
  display:flex;align-items:center;justify-content:center;color:var(--white);
  font-family:'Playfair Display',serif;font-style:italic;font-size:13.5px}

.site-header{position:absolute;left:0;top:38px;width:1200px;height:50px;background:var(--header)}
.brand{position:absolute;left:162px;top:0;height:50px;display:flex;align-items:center;color:var(--white);
  font-family:'Playfair Display',serif;font-weight:700;font-size:22px;white-space:nowrap}
.main-nav{position:absolute;left:466px;top:19px;display:flex;gap:18px}
.main-nav a{color:var(--white);text-decoration:none;font-weight:700;font-size:9.5px;text-transform:uppercase;white-space:nowrap}
.main-nav a.active{color:var(--lime-bright)}
.call{position:absolute;left:884px;top:8px;display:flex;align-items:center;gap:9px}
.call-icon{width:33px;height:33px;border-radius:50%;background:var(--lime-bright);display:flex;align-items:center;justify-content:center}
.call-label{color:var(--white);font-size:11.5px;line-height:1}
.call-number{color:var(--lime-bright);font-family:'Playfair Display',serif;font-weight:700;font-size:19px;line-height:1.1}

.categories{position:absolute;left:0;top:88px;width:208px;height:510px;background:var(--sidebar)}
.categories-title{height:40px;background:var(--sidebar-head);padding-left:42px;display:flex;align-items:center;
  color:var(--lime);font-family:'Playfair Display',serif;font-weight:700;font-size:15px}
.categories ul{list-style:none;padding:16px 0 0 42px}
.categories li{height:35px;font-size:12.5px;text-transform:uppercase;color:var(--ink)}

.hero{position:absolute;left:208px;top:88px;width:992px;height:510px;
  background:radial-gradient(ellipse at 50% 60%,#a8642a 0%,#7b4a26 35%,#3e3128 70%,#2c2622 100%)}
.hero-title{position:absolute;left:208px;top:294px;width:992px;text-align:center;color:var(--white);
  font-family:'Playfair Display',serif;font-weight:900;font-size:92px;line-height:1}

.lower-backdrop{position:absolute;left:0;top:780px;width:1200px;height:368px;
  background:linear-gradient(180deg,#ececec 0%,#e2decf 40%,#d6d2be 100%)}
.why-title{position:absolute;left:0;top:664px;width:1200px;text-align:center;color:var(--heading);
  font-family:'Playfair Display',serif;font-weight:700;font-size:43px}
.why-rule{position:absolute;left:499px;top:730px;width:202px;height:1px;background:var(--heading)}

.feature{position:absolute;border-radius:50%;overflow:hidden}
.feature-photo{position:absolute;inset:0}
.feature svg.icon{position:absolute;left:50%;top:44%;transform:translate(-50%,-50%)}
.feature p{position:absolute;left:0;width:100%;top:72%;text-align:center;color:var(--white);
  font-family:'Playfair Display',serif;font-weight:700;font-size:12.5px;line-height:20px}
.feature-left{left:245px;top:770px;width:254px;height:254px}
.feature-right{left:701px;top:770px;width:254px;height:254px}
.feature-mid-ring{position:absolute;left:464px;top:761px;width:272px;height:272px;border-radius:50%;background:var(--white)}
.feature-mid{left:472px;top:769px;width:256px;height:256px}

.footer-cats{position:absolute;left:0;top:1058px;width:1200px;display:flex;justify-content:center;
  font-family:'Playfair Display',serif;font-weight:700;font-size:9.5px;text-transform:uppercase;color:var(--ink)}
.footer-cats span+span::before{content:"|";margin:0 9px;font-weight:400}
.footer-nav{position:absolute;left:0;top:1085px;width:1200px;display:flex;justify-content:center;gap:21px}
.footer-nav a{color:var(--ink);text-decoration:none;font-size:9.5px;text-transform:uppercase}
.copyright{position:absolute;left:0;top:1110px;width:1200px;text-align:center;font-size:9.5px;color:var(--ink)}
.copyright .name{color:var(--lime)}
</style>
</head>
<body>

<div class="promo-bar">You can place your order over the phone. easy!</div>

<header class="site-header">
  <div class="brand">Meadowlark Harvest Co</div>
  <nav class="main-nav">
    <a class="active" href="#">Home</a>
    <a href="#">Our Customers</a>
    <a href="#">About Meadowlark Harvest Co</a>
    <a href="#">Contact Us</a>
  </nav>
  <div class="call">
    <div class="call-icon">
      <svg width="14" height="14" viewBox="0 0 24 24"><path fill="#fff" d="M6.6 10.8c1.4 2.8 3.8 5.1 6.6 6.6l2.2-2.2c.3-.3.7-.4 1-.2 1.1.4 2.3.6 3.6.6.6 0 1 .4 1 1V20c0 .6-.4 1-1 1C10.6 21 3 13.4 3 4c0-.6.4-1 1-1h3.5c.6 0 1 .4 1 1 0 1.3.2 2.5.6 3.6.1.3 0 .7-.2 1l-2.3 2.2z"/></svg>
    </div>
    <div>
      <div class="call-label">Call us now</div>
      <div class="call-number">02 5550 1842</div>
    </div>
  </div>
</header>

<aside class="categories">
  <div class="categories-title">ALL CATEGORIES</div>
  <ul>
    <li>Potatoes</li><li>Pumpkin</li><li>Carrot</li><li>Onion</li><li>Cabbage</li><li>Celery</li><li>Capsicum</li>
    <li>Zucchini</li><li>Mushroom</li><li>Spinach</li><li>Brocolli</li><li>Cauliflower</li><li>Mixes</li>
  </ul>
</aside>

<div class="hero" role="img" aria-label="Wicker basket of fresh vegetables and fruit on a rustic wooden table"></div>
<h1 class="hero-title">Fresh is Best !</h1>

<div class="lower-backdrop" role="img" aria-label="Faded photograph of assorted fresh vegetables"></div>
<h2 class="why-title">Why Choose us?</h2>
<div class="why-rule"></div>

<div class="feature feature-left">
  <div class="feature-photo" role="img" aria-label="Person holding a wooden crate of fresh vegetables" style="background:radial-gradient(circle at 40% 60%,#6d8a3a,#3d4b33 60%,#2e3530)"></div>
  <svg class="icon" width="80" height="80" viewBox="0 0 80 80" fill="none" stroke="#fff" stroke-width="3" stroke-linecap="round">
    <circle cx="46" cy="44" r="24"/><circle cx="46" cy="44" r="16"/>
    <rect x="40" y="10" width="12" height="6" rx="2"/><line x1="46" y1="16" x2="46" y2="20"/>
    <polyline points="46,34 46,44 53,48"/>
    <line x1="6" y1="36" x2="20" y2="36"/><line x1="2" y1="44" x2="18" y2="44"/><line x1="6" y1="52" x2="20" y2="52"/>
  </svg>
  <p>consistantly cut vegies<br>everytime</p>
</div>

<div class="feature-mid-ring"></div>
<div class="feature feature-mid">
  <div class="feature-photo" role="img" aria-label="Basket of fresh produce under a green tint" style="background:radial-gradient(circle at 50% 50%,#9cc63a,#86b325 70%,#7aa61f)"></div>
  <svg class="icon" width="90" height="84" viewBox="0 0 90 84" fill="none" stroke="#fff" stroke-width="3" stroke-linecap="round" stroke-linejoin="round">
    <path d="M45 4 L64 11 V27 C64 39 56 47 45 52 C34 47 26 39 26 27 V11 Z"/>
    <polyline points="37,28 43,34 54,22"/>
    <rect x="4" y="58" width="12" height="22" rx="2"/>
    <path d="M16 62 H34 C40 62 44 66 44 66 H58 C62 66 62 72 58 72 H44"/>
    <path d="M16 78 H48 L80 60 C84 58 86 62 82 65 L56 82"/>
  </svg>
  <p>We use fresh,<br>quality products</p>
</div>

<div class="feature feature-right">
  <div class="feature-photo" role="img" aria-label="Person holding a box of fresh vegetables ready for delivery" style="background:radial-gradient(circle at 50% 65%,#5e7a45,#3c4a3e 60%,#2f3a34)"></div>
  <svg class="icon" width="100" height="70" viewBox="0 0 100 70" fill="none" stroke="#fff" stroke-width="3" stroke-linecap="round" stroke-linejoin="round">
    <rect x="12" y="4" width="54" height="42" rx="3"/>
    <path d="M66 16 H82 L94 32 V52 H66"/>
    <line x1="12" y1="52" x2="66" y2="52"/>
    <circle cx="28" cy="56" r="7"/><circle cx="80" cy="56" r="7"/>
    <polyline points="28,24 36,32 50,18"/>
    <line x1="2" y1="44" x2="14" y2="44"/><line x1="6" y1="36" x2="12" y2="36"/>
  </svg>
  <p>we can deliver to your<br>premises</p>
</div>

<div class="footer-cats">
  <span>Potatoes</span><span>Pumpkin</span><span>Carrot</span><span>Onion</span><span>Cabbage</span><span>Celery</span><span>Capsicum</span><span>Zucchini</span><span>Mushroom</span><span>Spinach</span><span>Brocolli</span><span>Cauliflower</span><span>Mixes</span>
</div>
<nav class="footer-nav">
  <a href="#">Home</a><a href="#">Our Customers</a><a href="#">About Meadowlark Harvest Co</a><a href="#">Contact Us</a>
</nav>
<div class="copyright">© copyrights 2023 <span class="name">Meadowlark Harvest Co</span> &nbsp;| &nbsp;&nbsp; All rights reserved.</div>

</body>
</html>
```